Redesign of 3-4 page site for professional services firm

Our site is www.kestrelvaleadvisors.com. We currently have a simple page made with HostNimbo tools. But the tools are not able to generate the look and feel we desire. We need a home page similar to current that tells a little about our company, our experience and our team. We need a second page to show details of current and past transactions we have assisted our clients with. Currently this page reads like a word document but we would like for it to present in a cleaner fashion and liven it up with some images that link to the industry served. For example, a motorcycle outline in a circle for the powersports related transactions. We would like page to introduce each member of "Our Team" and highlight their experience with a photo of each person. If there is no photo available, we would like a placeholder to be their initials in a circle that can be updated later. We would also like a contact us section whether this is a different page or part of the home page.

Target Market(s)

Retirement minded business owners

Industry/Entity Type

Professional Services

Coding

Coded - Design and coding required

Requirements
Must have
• See project description. Must include a page or section for "Current Listings" and "Recently Completed Transactions" (can be same page)

```html
<!DOCTYPE html>
<html lang="en">
<head>
<meta charset="utf-8">
<title>Kestrel Vale Advisors — Strategically Navigating Business Exits</title>
<link rel="stylesheet" href="https://fonts.googleapis.com/css2?family=Josefin+Sans:wght@400;500;600;700&display=swap">
<style>
:root{
  --green:#1fb51f;
  --green-dark:#149a14;
  --red:#e41d1d;
  --yellow:#d9d900;
  --ink:#1b1b1b;
  --text:#2a2a2a;
  --grey-bg:#f3f3f4;
  --line:#bdbdbd;
  --white:#ffffff;
}
*{box-sizing:border-box;margin:0;padding:0}
html,body{width:1200px;height:4112px;overflow:hidden;background:var(--white)}
body{font-family:"Josefin Sans",Arial,sans-serif;color:var(--text)}
.page{position:relative;width:1200px;height:4112px;overflow:hidden}
.abs{position:absolute}

/* header */
.brand{position:absolute;display:flex;align-items:center;gap:10px;font-weight:600;color:var(--ink);letter-spacing:.5px}
.brand-mark{width:16px;height:16px;background:var(--green)}
.site-header .brand{left:104px;top:46px;font-size:30px}
.main-nav{position:absolute;top:50px;left:452px;display:flex;gap:66px;font-size:15px;font-weight:500;color:var(--ink);text-transform:uppercase}
.main-nav .active{position:relative}
.main-nav .active::after{content:"";position:absolute;left:0;right:0;bottom:-9px;height:2px;background:var(--red)}
.btn{display:inline-flex;align-items:center;justify-content:center;font-family:inherit;font-weight:600;text-transform:uppercase;color:var(--white);border:0;letter-spacing:.3px}
.btn-green{background:var(--green)}
.btn-red{background:var(--red)}
.nav-contact{position:absolute;left:932px;top:40px;width:154px;height:40px;font-size:15px}

/* hero */
.hero-photo{position:absolute;left:0;top:0;width:1200px;height:780px;
  background:linear-gradient(180deg,#ffffff 0%,rgba(255,255,255,.85) 18%,rgba(238,240,244,.4) 34%,transparent 50%),
  linear-gradient(90deg,#5a6b80 0%,#c7ae92 30%,#2c3550 52%,#b98a70 72%,#3b3f4a 100%)}
.hero-shape{position:absolute;left:0;top:640px}
.hero-kicker{position:absolute;top:156px;left:0;width:1200px;text-align:center;font-size:15px;letter-spacing:2px;color:var(--ink);text-transform:uppercase}
.hero-kicker span::before,.hero-kicker span::after{content:"";display:inline-block;width:30px;height:2px;background:var(--ink);vertical-align:middle;margin:0 8px}
.hero-title{position:absolute;top:178px;left:0;width:1200px;text-align:center;font-weight:600;text-transform:uppercase;line-height:52px}
.hero-title .accent{display:block;color:var(--green);font-size:47px}
.hero-title .main{display:block;color:var(--ink);font-size:47px}
.hero-cta{position:absolute;left:499px;top:291px;width:210px;height:44px;font-size:15px}

/* section headings */
.kicker{font-size:15px;letter-spacing:2px;color:var(--red);text-transform:uppercase}
.section-title{font-size:42px;font-weight:500;color:var(--ink);text-transform:uppercase;letter-spacing:.5px}
.section-title b{font-weight:700}
.title-rule{width:64px;height:3px;background:var(--yellow)}
.center-head{position:absolute;left:0;width:1200px;text-align:center}
.center-head .title-rule{margin:10px auto 0}

/* about */
.about-art{position:absolute;left:60px;top:840px;width:460px;height:504px;
  background:radial-gradient(ellipse at 45% 70%,#e9e9e9 0%,#f6f6f6 45%,#ffffff 75%)}
.about-copy{position:absolute;left:600px;top:900px;width:520px;font-size:17px;line-height:24px;color:var(--text)}
.about-copy p{margin-bottom:22px}
.quote{border-left:2px solid var(--red);padding-left:16px}
.about-cta{position:absolute;left:590px;top:1216px;width:202px;height:52px;font-size:18px}

/* experience */
.experience{position:absolute;left:0;top:1344px;width:1200px;height:1077px;background:
  radial-gradient(ellipse at 80% 80%,#e4e6ea 0%,transparent 55%),var(--grey-bg)}
.timeline-line{position:absolute;left:598px;top:1497px;width:2px;height:740px;background:var(--line)}
.step{position:absolute;width:100px;height:100px;border-radius:50%;background:var(--white);display:flex;align-items:center;justify-content:center}
.step .dot{width:86px;height:86px;border-radius:50%;display:flex;align-items:center;justify-content:center;border:3px solid var(--white)}
.step.red{border:2px solid var(--red)} .step.red .dot{background:var(--red)}
.step.yellow{border:2px solid var(--yellow)} .step.yellow .dot{background:var(--yellow)}
.step.green{border:2px solid var(--green)} .step.green .dot{background:var(--green)}
.step-text{position:absolute;font-size:18px;line-height:23px;color:var(--text);width:440px}
.step-text.right{left:672px}
.step-text.left{left:100px;text-align:right;width:420px}

/* team */
.team-photo{position:absolute;left:551px;top:2421px;width:649px;height:640px;
  clip-path:polygon(0 13%,70% 0,100% 0,100% 100%,0 100%);
  background:linear-gradient(135deg,#c9b59a 0%,#8a7a68 35%,#3a3e4a 60%,#d8c9a8 85%,#e8e39a 100%)}
.team-accent{position:absolute;left:0;top:2421px}
.team-kicker{position:absolute;left:120px;top:2520px}
.team-title{position:absolute;left:118px;top:2546px;font-size:46px;font-weight:600;color:var(--ink)}
.team-copy{position:absolute;left:120px;top:2630px;width:430px;font-size:18px;line-height:25px}
.team-copy p{margin-bottom:24px}
.team-cta{position:absolute;left:116px;top:2893px;width:208px;height:53px;font-size:19px}

/* contact */
.contact-bg{position:absolute;left:0;top:3061px}
.contact-title{position:absolute;left:0;top:3128px;width:1200px;text-align:center;color:var(--white);font-size:40px;font-weight:600;text-transform:uppercase}
.contact-title .title-rule{margin:10px auto 0}
.field{position:absolute;height:58px;background:var(--white);display:flex;align-items:center;gap:12px;padding-left:22px;font-size:17px;color:var(--ink)}
.field svg{flex:none}
.field.area{align-items:flex-start;padding-top:22px}
.send{position:absolute;left:476px;top:3510px;width:250px;height:60px;font-size:18px;letter-spacing:1.5px}

/* footer */
.site-footer .brand{left:128px;top:3792px;font-size:28px}
.socials{position:absolute;left:124px;top:3864px;display:flex;gap:26px}
.socials span{width:24px;height:24px;border-radius:50%;background:var(--ink)}
.foot-col{position:absolute;top:3774px;font-size:14px;line-height:27px;color:var(--ink)}
.foot-col h3{font-size:15px;font-weight:600;text-transform:uppercase;border-left:3px solid var(--green);padding-left:8px;margin-bottom:12px;line-height:16px}
.foot-col ul{list-style:none;padding-left:13px}
.contact-item{display:flex;gap:10px;align-items:flex-start;font-size:13px;line-height:18px;margin-bottom:16px}
.contact-item i{flex:none;width:24px;height:24px;border-radius:50%;background:var(--red);display:flex;align-items:center;justify-content:center}
.signup{position:absolute;left:888px;top:3814px;width:262px;height:44px;border:1px solid #bbb;font-size:13px;padding-left:20px;display:flex;align-items:center;color:#555}
.subscribe{position:absolute;left:892px;top:3872px;width:148px;height:40px;font-size:14px}
.copyright{position:absolute;left:0;top:4019px;width:1200px;border-top:1px solid #999;padding-top:26px;text-align:center;font-size:14px;color:var(--ink)}
.to-top{position:absolute;left:1094px;top:4042px}
</style>
</head>
<body>
<div class="page">

  <!-- hero -->
  <div class="hero-photo" role="img" aria-label="Photo of a business team in discussion around a meeting table"></div>
  <svg class="hero-shape" width="1200" height="220" viewBox="0 0 1200 220" aria-hidden="true">
    <polygon points="0,95 600,25 1200,95 1200,135 600,55 0,135" fill="#d9d900"/>
    <polygon points="0,135 600,50 1200,135 1200,220 0,220" fill="#ffffff"/>
  </svg>

  <header class="site-header">
    <div class="brand"><span class="brand-mark"></span>Kestrel Vale</div>
    <nav class="main-nav">
      <span class="active">Home</span>
      <span>Business Listings</span>
      <span>Our Team</span>
    </nav>
    <a class="btn btn-green nav-contact">Contact Us</a>
  </header>

  <div class="hero-kicker"><span>Welcome to Kestrel Vale</span></div>
  <h1 class="hero-title"><span class="accent">Strategically Navigating</span><span class="main">Business Exits</span></h1>
  <a class="btn btn-red hero-cta">Get Started Today</a>

  <!-- about -->
  <div class="center-head" style="top:748px">
    <div class="kicker">Who we are</div>
    <h2 class="section-title">About <b>Kestrel Vale</b></h2>
    <div class="title-rule"></div>
  </div>
  <div class="about-art" role="img" aria-label="Illustration of red, yellow and green arrows rising over a handshake"></div>
  <div class="about-copy">
    <p>At Kestrel Vale Advisors, our mission is to empower entrepreneurs and business owners by facilitating seamless transactions that lead to mutual success.</p>
    <p>With a commitment to integrity, transparency, and unmatched professionalism, we strive to create a positive and rewarding experience for all our clients.</p>
    <p class="quote">We understand that selling or acquiring a business can be a complex and emotional journey, which is why our dedicated team of experts is here to guide you every step of the way.</p>
  </div>
  <a class="btn btn-green about-cta">Learn More</a>

  <!-- experience -->
  <section class="experience" aria-label="Our experience"></section>
  <div class="center-head" style="top:1394px">
    <div class="kicker">Who we are</div>
    <h2 class="section-title">Our <b>Experience</b></h2>
    <div class="title-rule"></div>
  </div>
  <div class="timeline-line"></div>

  <div class="step red" style="left:549px;top:1543px"><div class="dot">
    <svg width="40" height="40" viewBox="0 0 40 40" fill="none" stroke="#fff" stroke-width="2"><circle cx="14" cy="14" r="6"/><path d="M4 34c0-7 4-11 10-11s10 4 10 11"/><rect x="24" y="6" width="12" height="9"/></svg>
  </div></div>
  <p class="step-text right" style="top:1562px">With decades of experience Kestrel Vale Advisors has proudly assisted numerous clients in successfully navigating the intricate journey of selling their businesses.</p>

  <div class="step yellow" style="left:549px;top:1701px"><div class="dot">
    <svg width="40" height="40" viewBox="0 0 40 40" fill="none" stroke="#fff" stroke-width="2"><circle cx="20" cy="20" r="14"/><circle cx="13" cy="18" r="3"/><circle cx="20" cy="16" r="3"/><circle cx="27" cy="18" r="3"/><path d="M9 28c1-4 7-5 11-5s10 1 11 5"/></svg>
  </div></div>
  <p class="step-text left" style="top:1722px">Our team brings a wealth of knowledge and expertise acquired through years of working closely with entrepreneurs and business owners across diverse industries.</p>

  <div class="step green" style="left:549px;top:1859px"><div class="dot">
    <svg width="40" height="40" viewBox="0 0 40 40" fill="none" stroke="#fff" stroke-width="2"><path d="M4 16l8-6 8 4 8-4 8 6"/><path d="M10 20l8 8c2 2 4 2 6 0l6-6"/><path d="M16 18l6 6"/></svg>
  </div></div>
  <p class="step-text right" style="top:1878px">We understand the unique challenges and complexities involved in selling a business, from valuation and marketing to negotiations and closing the deal.</p>

  <div class="step red" style="left:549px;top:2015px"><div class="dot">
    <svg width="40" height="40" viewBox="0 0 40 40" fill="none" stroke="#fff" stroke-width="2"><path d="M24 6v18"/><path d="M24 6h10l-3 4 3 4H24"/><circle cx="10" cy="30" r="4"/><path d="M14 30h6l4-6"/></svg>
  </div></div>
  <p class="step-text left" style="top:2032px">We take pride in our track record of delivering exceptional results and helping our clients achieve their desired outcomes.</p>

  <div class="step green" style="left:549px;top:2164px"><div class="dot">
    <svg width="40" height="40" viewBox="0 0 40 40" fill="none" stroke="#fff" stroke-width="2"><circle cx="20" cy="17" r="9"/><path d="M16 30h8M17 34h6"/><path d="M20 4v-2M8 8l-2-2M32 8l2-2M4 17H2M36 17h2"/></svg>
  </div></div>
  <p class="step-text right" style="top:2170px">Our extensive experience allows us to anticipate potential obstacles and proactively find solutions, ensuring a seamless and efficient process for our clients.</p>

  <!-- team -->
  <svg class="team-accent" width="1200" height="640" viewBox="0 0 1200 640" aria-hidden="true">
    <defs><linearGradient id="teamGlow" x1="0" y1="0" x2="1" y2="1"><stop offset="0" stop-color="#d9d900"/><stop offset="1" stop-color="#1fb51f"/></linearGradient></defs>
    <polygon points="1010,0 1200,0 1200,640 760,640" fill="url(#teamGlow)"/>
  </svg>
  <div class="team-photo" role="img" aria-label="Photo of the advisory team gathered around a laptop"></div>
  <div class="kicker team-kicker">Meet our team</div>
  <h2 class="team-title">OUR TEAM</h2>
  <div class="team-copy">
    <p>Together, our team of CPAs, attorneys, real estate brokers, and financial advisors work collaboratively to provide you with a holistic approach to business transactions.</p>
    <p class="quote">With our combined knowledge and experience, we strive to ensure a smooth and successful journey for our clients, delivering exceptional results and peace of mind.</p>
  </div>
  <a class="btn btn-green team-cta">Learn More</a>

  <!-- contact -->
  <svg class="contact-bg" width="1200" height="680" viewBox="0 0 1200 680" aria-hidden="true">
    <defs><linearGradient id="greenBand" x1="0" y1="0" x2="1" y2="1"><stop offset="0" stop-color="#2ec02e"/><stop offset="1" stop-color="#17a317"/></linearGradient></defs>
    <polygon points="0,530 600,640 1200,530 1200,556 600,662 0,556" fill="#e41d1d"/>
    <polygon points="0,0 1200,0 1200,540 600,640 0,540" fill="url(#greenBand)"/>
  </svg>
  <h2 class="contact-title">Leave us a message<div class="title-rule"></div></h2>

  <form aria-label="Contact form">
    <div class="field" style="left:228px;top:3211px;width:366px">
      <svg width="18" height="18" viewBox="0 0 18 18" fill="#9a9a9a"><circle cx="9" cy="5" r="4"/><path d="M1 18c0-5 4-7 8-7s8 2 8 7z"/></svg>First Name*</div>
    <div class="field" style="left:608px;top:3211px;width:366px">
      <svg width="18" height="18" viewBox="0 0 18 18" fill="#9a9a9a"><circle cx="9" cy="5" r="4"/><path d="M1 18c0-5 4-7 8-7s8 2 8 7z"/></svg>Last Name*</div>
    <div class="field" style="left:228px;top:3283px;width:366px">
      <svg width="20" height="16" viewBox="0 0 20 16" fill="#9a9a9a"><path d="M0 2h20v12H0z"/><path d="M0 2l10 7 10-7" stroke="#fff" stroke-width="1.5" fill="none"/></svg>Email address*</div>
    <div class="field" style="left:608px;top:3283px;width:366px">
      <svg width="18" height="18" viewBox="0 0 18 18" fill="#9a9a9a"><path d="M4 1l3 4-2 2c1 3 3 5 6 6l2-2 4 3-2 3C8 17 1 10 1 3z"/></svg>Phone*</div>
    <div class="field area" style="left:228px;top:3355px;width:748px;height:136px">
      <svg width="20" height="18" viewBox="0 0 20 18" fill="#9a9a9a"><ellipse cx="10" cy="8" rx="10" ry="7"/><path d="M3 12l-2 6 6-3z"/></svg>Leave Message</div>
    <button class="btn btn-red send" type="submit">Send Message &#8250;</button>
  </form>

  <!-- footer -->
  <footer class="site-footer">
    <div class="brand"><span class="brand-mark"></span>Kestrel Vale</div>
    <div class="socials" aria-label="Social links"><span></span><span></span><span></span><span></span></div>

    <div class="foot-col" style="left:386px">
      <h3>Navgation</h3>
      <ul><li>Home</li><li>Business Listings</li><li>Our Team</li><li>Contact Us</li></ul>
    </div>

    <div class="foot-col" style="left:578px;width:280px">
      <h3>Contact Us</h3>
      <div class="contact-item" style="padding-left:10px"><i><svg width="10" height="12" viewBox="0 0 10 12" fill="#fff"><path d="M5 0a5 5 0 015 5c0 3-5 7-5 7S0 8 0 5a5 5 0 015-5z"/></svg></i><span>482 Larkspur Lane, Ridgefield,<br>Oklahoma 74012, United States</span></div>
      <div class="contact-item" style="padding-left:10px"><i><svg width="12" height="12" viewBox="0 0 18 18" fill="#fff"><path d="M4 1l3 4-2 2c1 3 3 5 6 6l2-2 4 3-2 3C8 17 1 10 1 3z"/></svg></i><span style="padding-top:4px">405-555-0148</span></div>
      <div class="contact-item" style="padding-left:10px"><i><svg width="12" height="10" viewBox="0 0 20 16" fill="#fff"><path d="M0 2h20v12H0z"/></svg></i><span style="padding-top:4px">enquiry@kestrelvaleadvisors.com</span></div>
    </div>

    <div class="foot-col" style="left:878px">
      <h3>Sign up for updates</h3>
    </div>
    <div class="signup">Email address</div>
    <a class="btn btn-red subscribe">Subscribe &#8250;</a>

    <p class="copyright">Copyright © 2025 Kestrel Vale Advisors. All Rights Reserved</p>
    <svg class="to-top" width="16" height="22" viewBox="0 0 16 22" fill="none" stroke="#d9d900" stroke-width="2.5" aria-label="Back to top"><path d="M8 21V2M1 9l7-7 7 7"/></svg>
  </footer>
</div>
</body>
</html>
```